Label or packaging Design for Hair Care Line

Dear Designer,
We are Corvella, a brand known for our premium hairstyling tools, and we are excited to expand into hair care. We are currently looking for a talented designer to create the label designs for our entire luxury hair care line.
This project is crucial in establishing our visual identity in the hair care market, and we aim to position ourselves alongside premium brands such as LTP, Dorvane Hair Atelier, and Pelmi.
Project Scope
We need a cohesive label design for our hair care line, which includes:
5 products (e.g., shampoo, conditioner, hair oil, styling cream, and a hair mask).
The designs should include:
Front label: Highlighting the product name, key features, and branding.
Our goal is to achieve a design that communicates premium luxury with a touch of professionalism. Below are the specific guidelines to help you align with our vision:
Style and Inspiration
Think of brands like LTP, Dorvane Hair Atelier, and Pelmi.
Luxury and Minimalism: Clean lines, sophisticated typography, and an elegant color palette.
Subtle femininity: premium finishes like metallic accents (gold, silver, or rose gold).
Brand Personality
Premium: Reflecting high quality and exclusivity.
Modern & Professional: Appealing to a refined, professional audience but also suitable for lifestyle-oriented customers.
Warm & Empowering: A brand that celebrates confidence and individuality.
Color Palette
Neutral tones like black, white, accented with metallics (gold or silver) for a luxurious feel.
Colors that feel timeless and elegant rather than trendy or overly bright.
Typography
Use clean, modern fonts (preferably sans-serif or serif for a refined look).
Clear and legible for all product details while maintaining a high-end aesthetic.
Materials and Finishes
Packaging Shape
The label designs should suit a variety of bottle and jar shapes (e.g., cylindrical, flat, or rounded).
Keep scalability in mind so the identity remains consistent across different products.
Deliverables
To understand the aesthetic we are aiming for, here are some brands to use as inspiration:
LTP: For its minimalistic and modern approach.
Dorvane Hair Atelier: For its combination of luxury and professional appeal.
Pelmi: For its soft femininity and lifestyle branding.
we would like to see your designs applied to a variety of packaging types to get an overall impression of how the brand identity works across different product formats. This includes:
A squeeze bottle (e.g., for styling creams or conditioners).
A glass bottle with a dropper (e.g., for a luxurious hair oil).
A shampoo/conditioner bottle (standard pump or flip-top cap).
A spray bottle (e.g., for leave-in treatments or heat protectors).
By creating designs for these different packaging types, we can better evaluate how cohesive and versatile the brand identity will be across the entire product line.

Updates
As you may have noticed from the designs, they don’t quite align with our briefing. The look needs to be clean and professional, similar to Dorvane, LTP, and the other examples we provided. Please address this, and we’ll check it!

Target Market(s)
europe and us
Font styles to use
Other font styles liked:
- century gothic

Look and feel
Each slider illustrates characteristics of the customer's brand and the style your logo design should communicate.

```html
<!DOCTYPE html>
<html lang="en">
<head>
<meta charset="utf-8">
<title>Corvella Hair Care Labels</title>
<link rel="stylesheet" href="https://fonts.googleapis.com/css2?family=Josefin+Sans:wght@400;600;700&display=swap">
<style>
  :root {
    --backdrop: #e8655a;
    --label: #ffffff;
    --ink: #1d1d1f;
    --gold: #d2a64a;
    --soft-shadow: rgba(120, 30, 25, 0.18);
  }
  * { margin: 0; padding: 0; box-sizing: border-box; }
  html, body {
    width: 1200px;
    height: 1200px;
    overflow: hidden;
    background: var(--backdrop);
    font-family: "Josefin Sans", "Century Gothic", sans-serif;
    color: var(--ink);
  }
  .canvas { position: relative; width: 1200px; height: 1200px; }
  .label {
    position: absolute;
    background: var(--label);
    box-shadow: 0 10px 30px var(--soft-shadow);
    display: flex;
    flex-direction: column;
    align-items: center;
    text-align: center;
  }
  .wordmark {
    font-weight: 400;
    letter-spacing: 0.02em;
    color: var(--ink);
    text-transform: lowercase;
  }
  .category {
    font-weight: 700;
    letter-spacing: 0.08em;
    text-transform: uppercase;
    color: var(--ink);
  }
  .product-name {
    font-weight: 700;
    letter-spacing: 0.08em;
    text-transform: uppercase;
    color: var(--gold);
    line-height: 1.15;
  }
  .ingredients {
    font-weight: 600;
    text-transform: uppercase;
    letter-spacing: 0.06em;
    line-height: 1.55;
    color: var(--ink);
  }
  .volume {
    font-weight: 700;
    letter-spacing: 0.1em;
    text-transform: uppercase;
    color: var(--ink);
  }

  /* Serum dropper label */
  .label--serum { left: 70px; top: 90px; width: 330px; height: 230px; justify-content: center; gap: 14px; }
  .label--serum .wordmark { font-size: 40px; }
  .label--serum .category { font-size: 15px; }
  .label--serum .product-name { font-size: 17px; margin-top: -8px; }
  .label--serum .volume { font-size: 11px; }

  /* Shampoo tube front */
  .label--tube { left: 70px; top: 370px; width: 330px; height: 750px; border-radius: 6px 6px 2px 2px; padding: 110px 36px 70px; }
  .label--tube .wordmark { font-size: 44px; }
  .label--tube .category { font-size: 15px; margin-top: 140px; }
  .label--tube .product-name { font-size: 17px; margin-top: 6px; }
  .label--tube .ingredients { font-size: 8.5px; margin-top: 100px; }
  .label--tube .volume { font-size: 11px; margin-top: auto; }

  /* Argan elixir dropper label */
  .label--elixir { left: 445px; top: 450px; width: 310px; height: 300px; justify-content: center; gap: 14px; }
  .label--elixir .wordmark { font-size: 42px; }
  .label--elixir .category { font-size: 15px; margin-top: 6px; }
  .label--elixir .product-name { font-size: 17px; margin-top: -8px; }
  .label--elixir .volume { font-size: 11px; margin-top: 8px; }

  /* Pump bottle front */
  .label--pump { left: 800px; top: 230px; width: 330px; height: 780px; border-radius: 60px 60px 30px 30px; padding: 170px 36px 80px; }
  .label--pump .wordmark { font-size: 44px; }
  .label--pump .category { font-size: 15px; margin-top: 60px; }
  .label--pump .product-name { font-size: 17px; margin-top: 6px; }
  .label--pump .ingredients { font-size: 8.5px; margin-top: 90px; }
  .label--pump .volume { font-size: 11px; margin-top: 60px; }
</style>
</head>
<body>
<main class="canvas">

  <section class="label label--serum" aria-label="Overnight repair serum label">
    <div class="wordmark">corvella</div>
    <div class="category">Serum</div>
    <div class="product-name">Overnight<br>Repair</div>
    <div class="volume">30 ml. | 1.01 fl. oz</div>
  </section>

  <section class="label label--tube" aria-label="Moisturing shampoo tube">
    <div class="wordmark">corvella</div>
    <div class="category">Hair</div>
    <div class="product-name">Moisturing<br>Shampoo</div>
    <p class="ingredients">Argania spinosa kernel extract (argan elixir), silk amino acids (silk protein), panthenol (provitamin B), polyquaternium-53, dimethylpabamidopropyl laurdimonium tosylate, amodimethicone/morpholinomethyl silsesquioxane copolymer, polyquaternium-10</p>
    <div class="volume">50 ml. | 3.38 fl. oz</div>
  </section>

  <section class="label label--elixir" aria-label="Argan moisturing elixir label">
    <div class="wordmark">corvella</div>
    <div class="category">Argan</div>
    <div class="product-name">Moisturing<br>Elixir</div>
    <div class="volume">100 ml. | 3.38 fl. oz</div>
  </section>

  <section class="label label--pump" aria-label="Couture silk perfume pump bottle">
    <div class="wordmark">corvella</div>
    <div class="category">Hair</div>
    <div class="product-name">Couture<br>Silk Perfume</div>
    <p class="ingredients">Cyclopentasiloxane, dimethicone, argania spinoza kernel oil, silk amino acids, simmondsia chinensis (jojoba) seed oil, prunus amygdalus dulcis oil, ethylhexyl methoxycinnamate, parfum</p>
    <div class="volume">200 ml. | 3.38 fl. oz</div>
  </section>

</main>
</body>
</html>
```